Business Card for a Wedding Films Business

We require a business card design for our business 'Lewis Marrow Wedding Films'. The logo needs to look classy and high end.

Target Market(s)

Wedding Couples

Contact Information for Business Card

Lewis Marrow Wedding Films
07312 605 227
films@lewismarrowreels.com
www.lewismarrowreels.com

Facebook: @lewismarrowweddingfilms
Instagram: @lewismarrowfilms

Font styles to use
Sans Serif

Requirements
Must have
• Social media icons - Facebook and Instagram

```html
<!DOCTYPE html>
<html lang="en">
<head>
<meta charset="utf-8">
<title>Lewis Marrow Wedding Films – Business Card</title>
<link href="https://fonts.googleapis.com/css2?family=Jost:wght@400;500&family=Arimo:wght@400&display=swap" rel="stylesheet">
<style>
  :root {
    --page: #ebecee;
    --frame: #ffffff;
    --card: #000000;
    --ink: #ffffff;
    --pattern-light: #e6e6e6;
    --pattern-mid: #a8a8a8;
    --pattern-dark: #6e6e6e;
  }
  * { margin: 0; padding: 0; box-sizing: border-box; }
  html, body {
    width: 800px; height: 1200px; overflow: hidden;
    background: var(--page);
  }
  .board { position: relative; width: 800px; height: 1200px; }
  .card-frame {
    position: absolute; left: 62px; width: 698px; height: 420px;
    background: var(--frame);
  }
  .card-frame.front { top: 134px; }
  .card-frame.back { top: 641px; }
  .card {
    position: absolute; width: 655px; height: 376px;
    background: var(--card); overflow: hidden; color: var(--ink);
  }
  .front .card { left: 20px; top: 22px; }
  .back .card { left: 24px; top: 25px; }
  .pattern { position: absolute; left: 0; top: 0; width: 655px; height: 376px; }

  .wordmark {
    position: absolute; text-align: center;
    font-family: "Jost", sans-serif; color: var(--ink);
  }
  .wordmark .name {
    font-weight: 500; text-transform: uppercase; white-space: nowrap;
  }
  .wordmark .tagline {
    font-weight: 400; text-transform: uppercase; white-space: nowrap;
  }
  .front .wordmark { left: 318px; top: 192px; width: 280px; }
  .front .wordmark .name { font-size: 22px; letter-spacing: 4.5px; line-height: 1.1; }
  .front .wordmark .tagline { font-size: 9.5px; letter-spacing: 6.5px; margin-top: 5px; }
  .back .wordmark { left: 24px; top: 308px; width: 144px; }
  .back .wordmark .name { font-size: 12px; letter-spacing: 2.4px; line-height: 1.1; }
  .back .wordmark .tagline { font-size: 5.5px; letter-spacing: 3.4px; margin-top: 3px; }

  .contact {
    position: absolute; display: flex; align-items: center; gap: 9px;
    font-family: "Arimo", sans-serif; font-size: 11.5px; color: var(--ink);
    white-space: nowrap;
  }
  .contact svg { flex: none; }
  .contact.email { left: 212px; top: 331px; }
  .contact.phone { left: 486px; top: 329px; letter-spacing: 1.3px; gap: 12px; }

  .social-bar {
    position: absolute; height: 28px; right: 44px;
    background: var(--card); border-radius: 0 14px 14px 0;
    display: flex; align-items: center; gap: 14px; padding-left: 14px;
    font-family: "Arimo", sans-serif; font-size: 11.5px; color: var(--ink);
    white-space: nowrap;
  }
  .social-bar .dot {
    width: 12px; height: 12px; border-radius: 50%;
    border: 1.5px solid var(--ink); flex: none;
  }
  .social-bar.social-primary { top: 58px; left: 340px; }
  .social-bar.social-secondary { top: 126px; left: 385px; }
  .social-bar.website { top: 192px; left: 426px; }
</style>
</head>
<body>
<div class="board">

  <section class="card-frame front">
    <div class="card">
      <svg class="pattern" viewBox="0 0 655 376" role="img" aria-label="Geometric repeating triangle line pattern in white and grey">
        <defs>
          <linearGradient id="front-pattern" x1="0" y1="0" x2="1" y2="1">
            <stop offset="0" stop-color="var(--pattern-light)"/>
            <stop offset="0.5" stop-color="var(--pattern-mid)"/>
            <stop offset="1" stop-color="var(--pattern-dark)"/>
          </linearGradient>
        </defs>
        <polygon points="0,0 370,0 162,376 0,376" fill="url(#front-pattern)"/>
      </svg>

      <div class="wordmark">
        <div class="name">Lewis Marrow</div>
        <div class="tagline">Wedding Films</div>
      </div>

      <div class="contact email">
        <svg width="14" height="11" viewBox="0 0 14 11" aria-hidden="true">
          <rect x="0.75" y="0.75" width="12.5" height="9.5" fill="none" stroke="#fff" stroke-width="1"/>
          <polyline points="1,1 7,6 13,1" fill="none" stroke="#fff" stroke-width="1"/>
        </svg>
        <span>films@lewismarrowreels.com</span>
      </div>

      <div class="contact phone">
        <svg width="10" height="16" viewBox="0 0 10 16" aria-hidden="true">
          <rect x="0.75" y="0.75" width="8.5" height="14.5" rx="1.8" fill="none" stroke="#fff" stroke-width="1"/>
          <line x1="4" y1="12.8" x2="6" y2="12.8" stroke="#fff" stroke-width="1"/>
        </svg>
        <span>07312 605 227</span>
      </div>
    </div>
  </section>

  <section class="card-frame back">
    <div class="card">
      <svg class="pattern" viewBox="0 0 655 376" role="img" aria-label="Geometric repeating triangle line pattern in white and grey">
        <defs>
          <linearGradient id="back-pattern" x1="1" y1="0" x2="0" y2="1">
            <stop offset="0" stop-color="var(--pattern-light)"/>
            <stop offset="0.5" stop-color="var(--pattern-mid)"/>
            <stop offset="1" stop-color="var(--pattern-dark)"/>
          </linearGradient>
        </defs>
        <polygon points="286,0 655,0 655,376 490,376" fill="url(#back-pattern)"/>
      </svg>

      <div class="social-bar social-primary">
        <span class="dot"></span>
        <span>@lewismarrowweddingfilms</span>
      </div>
      <div class="social-bar social-secondary">
        <span class="dot"></span>
        <span>@lewismarrowfilms</span>
      </div>
      <div class="social-bar website">
        <svg width="14" height="14" viewBox="0 0 14 14" aria-hidden="true">
          <circle cx="7" cy="7" r="6" fill="none" stroke="#fff" stroke-width="1"/>
          <ellipse cx="7" cy="7" rx="2.6" ry="6" fill="none" stroke="#fff" stroke-width="1"/>
          <line x1="1" y1="7" x2="13" y2="7" stroke="#fff" stroke-width="1"/>
          <line x1="2" y1="4" x2="12" y2="4" stroke="#fff" stroke-width="0.8"/>
          <line x1="2" y1="10" x2="12" y2="10" stroke="#fff" stroke-width="0.8"/>
        </svg>
        <span>www.lewismarrowreels.com</span>
      </div>

      <div class="wordmark">
        <div class="name">Lewis Marrow</div>
        <div class="tagline">Wedding Films</div>
      </div>
    </div>
  </section>

</div>
</body>
</html>
```